Silent, Invisible and powerful domestic rangehoods

I want the brochure o convey to our potential clients that we were the first to create the silent domestic rangehood, then we took the next step and made the rangehood invisible (so it could not be seen in the kitchen). Finally we have developed external motor that is hidden from view. This brochure will rely heavily on visuals with less text.

Target Market(s)

Families who want quality quiet times with friend and other family members which is nowadays more often spent sitting in the kitchen area. Home renovators, home proud couples, individual who enjoy cooking

Industry/Entity Type

Retail

Requirements
Must have
• Family photos in the kitchen enjoy themselves, Mums with children in the kitchen whilst preparing meals.
Nice to have
• Photos of two males and or two females in the kitchen preparing meals..
High quality presentation appealing to a high end market
Should not have
• Please do not include too many words, in many cases a point form format would be preferable. The focus of this brochure should be on quality and long term value for money.

```html
<!DOCTYPE html>
<html lang="en">
<head>
<meta charset="utf-8">
<title>Stillhaus Silent Rangehoods – Cover Set</title>
<link href="https://fonts.googleapis.com/css2?family=Poppins:wght@500;600;700;800&family=Oswald:wght@500&display=swap" rel="stylesheet">
<style>
  :root {
    --backdrop: #a9aaae;
    --paper: #ffffff;
    --magenta: #d6197a;
    --magenta-soft: rgba(236, 150, 190, 0.55);
    --ink: #1f1f22;
    --grey-type: #a7a7aa;
    --white-type: #ffffff;
  }
  * { box-sizing: border-box; margin: 0; padding: 0; }
  html, body { width: 1200px; height: 801px; overflow: hidden; }
  body {
    background: var(--backdrop);
    font-family: "Poppins", Arial, sans-serif;
    position: relative;
  }
  .cover {
    position: absolute;
    width: 358px;
    height: 507px;
    background: var(--paper);
    overflow: hidden;
  }
  .cover--left   { left: 46px;  top: 95px; }
  .cover--middle { left: 427px; top: 95px; }
  .cover--right  { left: 806px; top: 93px; }

  .brand {
    position: absolute;
    display: flex;
    align-items: center;
    gap: 6px;
    color: var(--magenta);
    font-weight: 700;
    font-size: 21px;
    letter-spacing: 0.2px;
    line-height: 1;
  }
  .brand__mark {
    width: 10px; height: 10px;
    background: var(--magenta);
  }

  .photo {
    position: absolute;
  }
  .photo--left {
    left: 0; top: 168px; width: 358px; height: 273px;
    background: linear-gradient(120deg, #e9e6e4 0%, #d9d4d0 45%, #c9b7ac 70%, #e8e6e3 100%);
  }
  .photo--middle {
    left: 0; top: 0; width: 311px; height: 507px;
    background: linear-gradient(160deg, #cfcdcd 0%, #e6e2e1 35%, #c9b6a8 60%, #8d7f77 85%, #b9b5b4 100%);
  }
  .photo--right {
    left: 0; top: 183px; width: 358px; height: 238px;
    background: linear-gradient(110deg, #6f665e 0%, #c9b8a6 35%, #8c7a68 60%, #4e4640 85%, #7a6a58 100%);
  }
  .ring { position: absolute; pointer-events: none; }

  .headline {
    position: absolute;
    line-height: 1;
    white-space: nowrap;
  }
  .headline--silent { color: var(--magenta); font-weight: 800; }
  .headline--sub { color: var(--white-type); font-weight: 700; }

  /* left cover */
  .cover--left .h-beautiful { left: 104px; top: 213px; font-size: 16px; letter-spacing: 4px; }
  .cover--left .h-silent    { left: 62px;  top: 224px; font-size: 42px; letter-spacing: 6px; }
  .cover--left .h-powerful  { left: 65px;  top: 266px; font-size: 15px; letter-spacing: 3px; }
  .cover--left .h-range {
    left: 57px; top: 437px; font-size: 31px; font-weight: 700;
    letter-spacing: 6px; color: var(--grey-type);
  }

  /* middle cover */
  .cover--middle .h-silent    { left: 154px; top: 211px; font-size: 34px; letter-spacing: 5px; }
  .cover--middle .h-beautiful { left: 156px; top: 245px; font-size: 20px; letter-spacing: 4px; }
  .cover--middle .h-powerful  { left: 156px; top: 268px; font-size: 20px; letter-spacing: 4px; color: rgba(255,255,255,0.8); }
  .vertical-label {
    position: absolute;
    left: 339px; top: 424px;
    transform: translate(-50%, -50%) rotate(-90deg);
    font-family: "Oswald", Arial, sans-serif;
    font-weight: 500;
    font-size: 11px;
    letter-spacing: 12.4px;
    color: var(--ink);
    white-space: nowrap;
    transform-origin: center;
  }

  /* right cover */
  .cover--right .h-silent    { left: 202px; top: 330px; font-size: 34px; letter-spacing: 5px; }
  .cover--right .h-beautiful { left: 203px; top: 366px; font-size: 19px; letter-spacing: 3px; }
  .cover--right .h-powerful  {
    left: 0; top: 382px; font-size: 46px; font-weight: 800;
    letter-spacing: 8px; color: #5a4d42;
  }
  .cover--right .h-range-line {
    left: 38px; top: 462px; font-family: "Oswald", Arial, sans-serif;
    font-weight: 500; font-size: 11px; letter-spacing: 11px; color: var(--ink);
  }
</style>
</head>
<body>

  <!-- Cover 1 -->
  <section class="cover cover--left">
    <div class="brand" style="left:112px; top:79px;"><span class="brand__mark"></span>stillhaus</div>
    <div class="photo photo--left" role="img" aria-label="Photo of a mother lifting her young child in a bright white kitchen"></div>
    <svg class="ring" style="left:0; top:168px;" width="358" height="273" viewBox="0 0 358 273">
      <circle cx="150" cy="50" r="118" fill="none" stroke="var(--magenta-soft)" stroke-width="22"/>
    </svg>
    <div class="headline headline--sub h-beautiful">BEAUTIFUL</div>
    <div class="headline headline--silent h-silent">SILENT</div>
    <div class="headline headline--sub h-powerful">POWERFUL</div>
    <div class="headline h-range">RANGEHOODS</div>
  </section>

  <!-- Cover 2 -->
  <section class="cover cover--middle">
    <div class="photo photo--middle" role="img" aria-label="Photo of a couple in a kitchen, the father lifting their baby, with the rangehood product shown on the counter and a ceiling vent above"></div>
    <svg class="ring" style="left:0; top:0;" width="311" height="507" viewBox="0 0 311 507">
      <circle cx="190" cy="190" r="70" fill="none" stroke="var(--magenta-soft)" stroke-width="16"/>
      <circle cx="220" cy="380" r="95" fill="none" stroke="var(--magenta-soft)" stroke-width="20"/>
    </svg>
    <div class="brand" style="left:18px; top:22px;"><span class="brand__mark"></span>stillhaus</div>
    <div class="headline headline--silent h-silent">SILENT</div>
    <div class="headline headline--sub h-beautiful">BEAUTIFUL</div>
    <div class="headline headline--sub h-powerful">POWERFUL</div>
    <div class="vertical-label" style="top:174px;">SILENT RANGEHOODS</div>
  </section>

  <!-- Cover 3 -->
  <section class="cover cover--right">
    <div class="brand" style="left:123px; top:52px;"><span class="brand__mark"></span>stillhaus</div>
    <div class="photo photo--right" role="img" aria-label="Photo of a family in a warm wooden kitchen, the father holding a toddler while the mother feeds him, fresh vegetables in front"></div>
    <svg class="ring" style="left:0; top:183px;" width="358" height="238" viewBox="0 0 358 238">
      <circle cx="300" cy="60" r="75" fill="none" stroke="var(--magenta-soft)" stroke-width="18"/>
    </svg>
    <div class="headline headline--silent h-silent">SILENT</div>
    <div class="headline headline--sub h-beautiful">BEAUTIFUL</div>
    <div class="headline h-powerful">POWERFUL</div>
    <div class="headline h-range-line">SILENT RANGEHOODS</div>
  </section>

</body>
</html>
```